Brand New Product Needs Sales Focused Website Design

Looking for design of Homepage, Category Page & Product Page for single product sales focused website. TrendaCrate manufacture and distribute a brand new product to the market called FoldiPal-Crate which is a super strong, re-useable, folding & stacking plastic box which can be seen on our current website www.foldipal-crate.example FoldiPal-Crate was originally developed as an alternative to supermarket carrier bags and was pitched as a box for life against the other low end re-useable products. The original version was made from recycled plastic and pitched very much as environmental product. We are now taking a different direction and have re-designed the boxes in 5 bright and fashionable designs and although we still want the primary focus to be supermarket shopping we want to position the product as a design led, must have shopping and household accessory rather than a boring, cheap looking black plastic box. The new designs will still have the environmental benefits of being able to be re-used thousands of times and being 100% recyclable and save on the imminent 5p tax on carrier bags in the UK however the new designs will not be made from recycled material. Although the main use for FoldiPal-Crate is supermarket shopping it has a multitude of other uses especially where you need temporary storage - laundry, back of the car, moving house/students, gardening, days out, home office filing (will take A4 file), recycling and much more - FoldiPal-Crate is made out of super strong Polypropylene and can be easily washed and sanitised after use and can be folded and unfolded thousands of times and so will last for many years. FoldiPal-Crate is a product that needs to be seen in action to be understood so the web design must quickly and easily communicate what FoldiPal-Crate is and how it works - this can be done with video, images and copy. Our current website does not work for many reasons:- it is too busy, has too much information, tries too hard and ultimately isn't working. Any of the images off our current website can be supplied for use. Once the concept of the website is agreed I can get these photoshopped with the new designs. Pictures of new designs for reference will be attached to this brief. Ultimately we want the website to convert visitors to sales and therefore designers with a proven track record in this field are especially welcome to enter. We also have a Fileharbor folder with over 100 product and situation images in - please send email address and we will send an invite to the folder. Due to Christmas period this competition will be run over 15 days however we may choose to extend the deadline to account for the non working days. Any questions feel free to ask - we will respond within 24 hours where possible.

```html
<!DOCTYPE html>
<html lang="en">
<head>
<meta charset="utf-8">
<title>FoldiPal-Crate – Folding Box</title>
<link href="https://fonts.googleapis.com/css2?family=Arimo:wght@400;700&family=Carlito:wght@400;700&display=swap" rel="stylesheet">
<style>
:root{
  --red:#fe1e3e;
  --ink:#333333;
  --muted:#777777;
  --line:#d9d9d9;
  --black:#000000;
  --quote-bg:#f1eff0;
  --white:#ffffff;
  --social:#aaaaaa;
}
*{margin:0;padding:0;box-sizing:border-box}
html,body{width:1171px;height:1200px;overflow:hidden;background:var(--white)}
body{position:relative;font-family:"Arimo",Arial,sans-serif;color:var(--ink)}
.top-rule{position:absolute;left:0;top:0;width:1171px;height:4px;background:#222}
.abs{position:absolute}

/* header */
.brand{left:292px;top:20px;font-family:"Carlito",sans-serif;font-size:29px;line-height:34px;color:#444;white-space:nowrap}
.tagline{left:504px;top:33px;font-size:11px;color:var(--red);white-space:nowrap}
.promo{left:292px;top:59px;width:572px;height:72px;background:var(--red);color:var(--white);padding:15px 0 0 18px}
.promo p{font-size:12px;line-height:16px;white-space:nowrap}
.promo .uses{font-size:10px;line-height:13px}
.hero-crate{left:746px;top:28px;width:118px;height:118px;background:linear-gradient(160deg,#e6b64a 0%,#3d9b3a 30%,#1f46c8 55%,#142f8f 100%);border-radius:6px}
.nav-rule{left:292px;top:133px;width:572px;height:1px;background:var(--line)}
.nav span{position:absolute;top:144px;font-size:10px;color:#555;white-space:nowrap}
.buy-tab{left:602px;top:137px;width:86px;height:28px;background:var(--red);color:var(--white);font-weight:700;font-size:13px;display:flex;align-items:center;justify-content:center}

/* video */
.video{left:292px;top:166px;width:572px;height:232px;background:radial-gradient(ellipse at 50% 55%,#8fa3b0 0%,#8b8257 35%,#6f6747 70%,#5a5440 100%)}
.play{left:561px;top:266px}

/* cards */
.card{top:421px;width:176px;height:174px;border:1px solid var(--line);text-align:center;font-family:"Carlito",sans-serif}
.card .big{font-size:35px;color:#3a3a3a;margin-top:14px;line-height:40px}
.card .sub{font-size:11px;color:#555;margin-top:10px}
.card .small{font-size:7px;color:#555;line-height:10px;margin:10px 14px 0}
.card .btn{position:absolute;left:46px;top:130px;width:82px;height:25px;background:var(--red);color:var(--white);font-family:"Arimo",sans-serif;font-size:7.5px;font-weight:700;display:flex;align-items:center;justify-content:center}

/* how it works band */
.steps{left:0;top:616px;width:1171px;height:162px;background:var(--black)}
.steps h2{position:absolute;left:0;width:100%;top:25px;text-align:center;color:var(--white);font-size:8.5px;font-weight:700}
.tile{position:absolute;top:54px;width:106px;height:80px;background:var(--white);border-radius:4px}
.tile .photo{position:absolute;left:10px;top:8px;width:86px;height:56px;background:linear-gradient(180deg,#2f5de0,#1233a8);border-radius:2px}
.tile .label{position:absolute;left:0;width:100%;bottom:3px;text-align:center;font-family:Georgia,serif;font-size:8px;color:#111}

/* testimonial */
.quote{left:0;top:778px;width:1171px;height:138px;background:var(--quote-bg);text-align:center}
.quote .mark{font-family:Georgia,serif;font-size:40px;color:#444;margin-top:14px;line-height:40px}
.quote p{font-family:"Carlito",sans-serif;font-size:11px;color:#444;line-height:16px;margin-top:10px}
.quote .by{font-size:7px;margin-top:12px}

/* newsletter */
.news-label{left:292px;top:942px;font-size:11px;color:#333}
.news-input{left:352px;top:937px;width:143px;height:24px;border:1px solid #ccc;font-size:7px;color:#aaa;padding:8px 10px}
.news-btn{left:500px;top:937px;width:61px;height:24px;background:var(--red);color:var(--white);font-size:8px;font-weight:700;display:flex;align-items:center;justify-content:center}
.follow{left:693px;top:942px;font-size:11px}
.social{top:935px;width:27px;height:27px;border-radius:50%;background:var(--social)}
.red-rule{left:0;top:976px;width:1171px;height:3px;background:var(--red)}

/* footer */
.col h3{font-family:"Carlito",sans-serif;font-weight:400;font-size:14px;color:#333;margin-bottom:12px}
.col li{list-style:none;font-size:8px;color:var(--muted);line-height:18px}
.store p{font-size:8px;color:#555;line-height:12px}
.phone{font-size:22px;color:var(--red);margin:4px 0 14px;white-space:nowrap}
.bottom-rule{left:0;top:1152px;width:1171px;height:1px;background:var(--line)}
.copy{left:293px;top:1165px;font-size:6.5px;color:var(--muted)}
</style>
</head>
<body>
<div class="top-rule"></div>

<header>
  <div class="abs brand">FoldiPal-Crate</div>
  <div class="abs tagline">Ingenious &amp; Practical</div>
  <div class="abs promo">
    <p>At Last ! &nbsp;A Solid Featherlight <b>Folding Box</b>.</p>
    <p>So Many Everday Practical Uses...</p>
    <p class="uses">Grocery Shopping &nbsp;| &nbsp;Laundry &nbsp;| &nbsp;Gardening &nbsp;| &nbsp;Caravan &amp; Camping &nbsp;| &nbsp;And Much More...</p>
  </div>
  <div class="abs hero-crate" role="img" aria-label="Blue folding crate filled with groceries"></div>
  <div class="abs nav-rule"></div>
  <nav class="nav">
    <span style="left:292px">home</span>
    <span style="left:344px">category</span>
    <span style="left:408px">product</span>
    <span style="left:467px">guarantee</span>
    <span style="left:536px">contact us</span>
  </nav>
  <div class="abs buy-tab">BUY NOW</div>
</header>

<section>
  <div class="abs video" role="img" aria-label="Product video still: floral patterned crate with brand label"></div>
  <svg class="abs play" width="34" height="34" viewBox="0 0 34 34">
    <circle cx="17" cy="17" r="16" fill="#e8e8e8" opacity="0.85"/>
    <path d="M13 10 L24 17 L13 24 Z" fill="#333"/>
  </svg>
</section>

<section>
  <div class="abs card" style="left:292px">
    <div class="big">100%</div>
    <div class="sub">Recycled Plastic &amp; 100% Recyclable</div>
    <div class="small">We Use And Throw Away 8 Billion Polluting Carriers Each year Here In The UK! It's Time For This Practice To Stop!</div>
    <div class="btn">READ MORE</div>
  </div>
  <div class="abs card" style="left:490px">
    <div class="big">£14.99</div>
    <div class="sub">A Simple Basic Product</div>
    <div class="small">FoldiPal-Crate Is A Unique New British Invention And Is Manufactured In Peterborough In Britain.</div>
    <div class="btn">BUY NOW</div>
  </div>
  <div class="abs card" style="left:688px">
    <div class="big">Award<br>Winning</div>
    <div class="sub">Best New Product In Show</div>
    <div class="btn">READ MORE</div>
  </div>
</section>

<section class="abs steps">
  <h2>FROM FEATHERLIGHT FLAT-PACK TO RIGID STACKING BOX IN SECONDS!</h2>
  <div class="tile" style="left:308px"><div class="photo" role="img" aria-label="Folded flat crate"></div><div class="label">Folded</div></div>
  <div class="tile" style="left:418px"><div class="photo" role="img" aria-label="Hands opening the clip"></div><div class="label">Open The Clip</div></div>
  <div class="tile" style="left:527px"><div class="photo" role="img" aria-label="Pulling out the ends"></div><div class="label">Pull Out Ends</div></div>
  <div class="tile" style="left:636px"><div class="photo" role="img" aria-label="Sliding rails to lock"></div><div class="label">Slide Rails To Lock</div></div>
  <div class="tile" style="left:745px"><div class="photo" role="img" aria-label="Assembled crate stacking"></div><div class="label">Stacks Too!</div></div>
  <svg class="abs" style="left:0;top:0" width="1171" height="162">
    <g fill="none" stroke="#999" stroke-width="2">
      <path d="M404 118 l14 0 m-5 -4 l5 4 l-5 4"/>
      <path d="M514 118 l14 0 m-5 -4 l5 4 l-5 4"/>
      <path d="M623 118 l14 0 m-5 -4 l5 4 l-5 4"/>
      <path d="M732 118 l14 0 m-5 -4 l5 4 l-5 4"/>
    </g>
  </svg>
</section>

<section class="abs quote">
  <div class="mark">&ldquo;</div>
  <p>Lorem ipsum dolor sit amet conse ctetur adipisicing elit, sed do eiusmod tempor incididunt ut labore et<br>dolore magna aliqua. Ut enim ad minim veniam, quis nostrud exercitatio.</p>
  <p class="by">- Lorem ipsum dolor sit amet conse ctetu</p>
</section>

<section>
  <div class="abs news-label">Newsletter</div>
  <div class="abs news-input">your email</div>
  <div class="abs news-btn">Subscribe</div>
  <div class="abs follow">Follow us</div>
  <div class="abs social" style="left:757px"></div>
  <div class="abs social" style="left:796px"></div>
  <div class="abs social" style="left:836px"></div>
  <div class="abs red-rule"></div>
</section>

<footer>
  <div class="abs col" style="left:292px;top:1007px">
    <h3>Information</h3>
    <ul><li>Home</li><li>Contact Us</li><li>FAQ</li><li>Privacy Statement</li><li>Terms &amp; Conditions</li></ul>
  </div>
  <div class="abs col" style="left:446px;top:1007px">
    <h3>Categories</h3>
    <ul><li>What do you think?</li><li>Plastic Pollution</li><li>Videos</li><li>Lifetime Gurantee</li><li>Award winning</li></ul>
  </div>
  <div class="abs col store" style="left:692px;top:1007px">
    <h3>Store Information</h3>
    <p>Reg Design no 1995440 Patent a.p no<br>GB1202987.2</p>
    <p style="margin-top:10px">Call us now:</p>
    <div class="phone">0123-555-0190</div>
    <p>Email: info@foldipal-crate.example</p>
  </div>
  <div class="abs bottom-rule"></div>
  <div class="abs copy">Copyright © FoldiPal-Crate 2014. &nbsp;| &nbsp;Privacy Policy</div>
</footer>
</body>
</html>
```